Curtain & Design Studio Project…
I am looking for a new website design for a store front “Curtain & Design Studio” business. Their customer would walk in off the street to have curtains designed for their home or business. This is not an ecommerce website.
The website colors should be light blue, dark blue, white and maybe tan. Be creative.
The curtains they sell can be found at www.tavilinen.com and www.pommerly.com. Please use images from these two website.
Navigation:
Home
Our Studio
Our Services
Our Manufactures
TAVILI
Pommerly
Our Process
Testimonials
Refer a Client
Subscribe to our Newsletter
Our Blog – (Needed for Internet Marketing)
Contact Us
The website should have a large footer for internet marketing purposes.
Great designs. Thank you everyone. I have sent them all to the client and i am waiting for feedback. I will let everyone know as soon as possible.
Sorry for the delay everyone. The client has been on vacation and has not provided feedback yet. As soon as I have an update I will let everyone know.

```html
<!DOCTYPE html>
<html lang="en">
<head>
<meta charset="utf-8">
<title>Fold &amp; Thread Studio</title>
<link href="https://fonts.googleapis.com/css2?family=Crimson+Pro:ital,wght@0,300;1,300&family=Open+Sans:wght@400;600&family=PT+Sans+Narrow:wght@400;700&family=Pinyon+Script&display=swap" rel="stylesheet">
<style>
:root{
  --page:#d7e4e9;
  --white:#ffffff;
  --panel:#f4f4f4;
  --line:#e3e6e8;
  --teal:#5f9cb2;
  --accent:#6fb2c9;
  --tile:#7bbccc;
  --text:#8a8f93;
  --nav:#9aa7ad;
  --footer:#5e86a8;
  --footer-top:#e8eef2;
  --bar:#12385e;
  --photo-a:#c9b98f;
  --photo-b:#6b5c4c;
  --pattern-a:#2c4a78;
  --pattern-b:#9ab2d6;
}
*{box-sizing:border-box;margin:0;padding:0}
html,body{width:821px;height:1200px;overflow:hidden}
body{background:var(--page);font-family:"Open Sans",sans-serif;color:var(--text);position:relative}
.abs{position:absolute}
.header{left:101px;top:8px;width:618px;height:62px;background:var(--white);border:6px solid #eef2f4}
.logo{left:19px;top:6px;font-family:"Crimson Pro",serif;font-weight:300;color:var(--teal);font-size:24px;line-height:26px}
.logo small{display:block;font-size:10px;letter-spacing:3px;line-height:10px;margin-top:1px}
.nav{right:20px;top:21px;display:flex;gap:22px;font-family:"PT Sans Narrow",sans-serif;font-size:10px;letter-spacing:1.3px;color:var(--nav)}
.nav .current{color:var(--teal);font-weight:700}
.sheet{left:101px;top:82px;width:618px;height:888px;background:var(--white)}
.hero{left:8px;top:7px;width:603px;height:259px;background:linear-gradient(100deg,#efe3c6 0%,var(--photo-a) 35%,#8a7a66 60%,var(--photo-b) 80%,#4d6a3a 100%)}
.hero-band{left:0;bottom:0;width:100%;height:46px;background:rgba(235,235,235,.72);font-family:"Crimson Pro",serif;font-style:italic;font-weight:300;font-size:21px;color:var(--teal);text-align:center;line-height:46px}
.welcome{left:9px;top:283px;width:395px;height:211px;background:var(--panel);padding:8px 19px}
.welcome h1{font-family:"Crimson Pro",serif;font-weight:300;font-size:18px;color:#7b8287;padding-bottom:4px;border-bottom:1px solid var(--line)}
.sub{font-family:"PT Sans Narrow",sans-serif;font-weight:700;font-size:9px;letter-spacing:1.6px;color:var(--accent);text-transform:uppercase}
.welcome .sub{margin:9px 0 6px}
.copy{font-size:7.3px;line-height:16.8px}
.welcome .copy{width:355px}
.more{font-size:7.5px;color:var(--accent);display:block}
.welcome .more{margin-top:2px}
.tile{left:415px;width:193px;height:67px;background:var(--tile);color:var(--white);font-family:"PT Sans Narrow",sans-serif;font-size:18px;letter-spacing:1px;text-align:center;line-height:67px}
.gallery{left:9px;top:507px;width:599px;height:368px;background:var(--panel);padding:10px 19px}
.gallery .sub{border-bottom:1px solid var(--line);width:366px;padding-bottom:4px;margin-bottom:4px}
.gallery .copy{width:366px}
.card{width:128px;height:130px;background:var(--white);border:1px solid #ececec}
.card .img{height:95px;background:radial-gradient(circle,var(--pattern-b) 20%,var(--pattern-a) 75%)}
.card p{font-size:7.5px;padding:4px 0 0 16px;line-height:13px}
.card .more{padding-left:16px}
.footer{left:0;top:988px;width:821px;height:180px;background:var(--footer);border-top:3px solid var(--footer-top)}
.fcol{top:17px;color:var(--white);font-size:7px}
.fcol h2{font-family:"PT Sans Narrow",sans-serif;font-size:9px;letter-spacing:1.6px;color:#c4d5e3;font-weight:400;padding-bottom:4px;border-bottom:1px dotted #c4d5e3;margin-bottom:5px}
.fcol li{list-style:none;display:flex;align-items:center;gap:6px;height:17px;font-weight:600}
.fcol li.ind{padding-left:15px}
.script{font-family:"Pinyon Script",cursive;font-size:20px;line-height:24px;margin:6px 0 3px}
.signup{display:flex;width:181px;height:21px}
.signup span{flex:1;background:var(--white);color:#999;font-style:italic;font-size:7.5px;line-height:21px;padding-left:8px}
.signup i{width:20px;background:var(--bar)}
.sq{width:12px;height:12px;background:#c9d8e4;display:inline-block}
.bar{left:0;top:1168px;width:821px;height:32px;background:var(--bar);font-size:7.5px;color:#8ea4b8;font-weight:600}
.bar .links{left:128px;top:14px;display:flex;gap:12px}
.bar .links .current,.bar .copy-note b{color:var(--white)}
.bar .copy-note{left:563px;top:14px}
</style>
</head>
<body>
<header class="abs header">
  <div class="abs logo">Fold &amp; Thread<small>design studio</small></div>
  <nav class="abs nav"><span class="current">Home</span><span>Studio</span><span>Services</span><span>Brands</span><span>Process</span><span>Blog</span><span>Contact</span></nav>
</header>

<main class="abs sheet">
  <section class="abs hero" role="img" aria-label="Photo of a living room with sheer curtains, a patterned sofa, lamp and plant">
    <div class="abs hero-band">Beautiful curtains expertly designed for your home or business</div>
  </section>

  <section class="abs welcome">
    <h1>Welcome to our site</h1>
    <h2 class="sub">Subheadline here</h2>
    <p class="copy">Lorem ipsum dolor sit amet, consectetur adipiscing elit. Fusce eleifend nisi at neque blandit tempus. Quisque ornare consectetur elit, ac imperdiet tellus suscipit vitae. Sed faucibus, diam at cursus fringilla, neque urna auctor neque, sit amet aliquet risus risus non massa. Nunc ante ante, fermentum vel lobortis ut, egestas et purus. Phasellus at felis libero. Aliquam ac augue libero, vitae posuere mauris. Proin nec fringilla turpis. In rhoncus gravida leo ut mollis. Nam dignissim suscipit est nec porttitor. Nullam quis nunc dolor. In erat orci, faucibus ac varius sit amet, mollis tincidunt dui. Pellentesque habitant morbi tristique senectus et netus et malesuada fames ac turpis egestas.</p>
    <span class="more">Read more &rarr;</span>
  </section>

  <a class="abs tile" style="top:283px">SEARCH DESIGNS</a>
  <a class="abs tile" style="top:355px">SUBSCRIBE</a>
  <a class="abs tile" style="top:427px">REFER A CLIENT</a>

  <section class="abs gallery">
    <h2 class="sub">Picture headline will go here</h2>
    <p class="copy">Lorem ipsum dolor sit amet, consectetur adipiscing elit. Fusce eleifend nisi at neque blandit tempus uisque ornare consectetur elit, ac imperdiet tellus suscipit vitae. Sed faucibus, diam at cursus fringilla.</p>
  </section>

  <div class="abs card" style="left:28px;top:576px"><div class="img" role="img" aria-label="Blue and tan fabric pattern swatch"></div><p>Uisque ornare consectetur</p><span class="more">Read more &rarr;</span></div>
  <div class="abs card" style="left:173px;top:576px"><div class="img" role="img" aria-label="Blue and tan fabric pattern swatch"></div><p>Uisque ornare consectetur</p><span class="more">Read more &rarr;</span></div>
  <div class="abs card" style="left:316px;top:576px"><div class="img" role="img" aria-label="Blue and tan fabric pattern swatch"></div><p>Uisque ornare consectetur</p><span class="more">Read more &rarr;</span></div>
  <div class="abs card" style="left:460px;top:576px"><div class="img" role="img" aria-label="Blue and tan fabric pattern swatch"></div><p>Uisque ornare consectetur</p><span class="more">Read more &rarr;</span></div>
  <div class="abs card" style="left:28px;top:716px"><div class="img" role="img" aria-label="Blue and tan fabric pattern swatch"></div><p>Uisque ornare consectetur</p><span class="more">Read more &rarr;</span></div>
  <div class="abs card" style="left:173px;top:716px"><div class="img" role="img" aria-label="Blue and tan fabric pattern swatch"></div><p>Uisque ornare consectetur</p><span class="more">Read more &rarr;</span></div>
  <div class="abs card" style="left:316px;top:716px"><div class="img" role="img" aria-label="Blue and tan fabric pattern swatch"></div><p>Uisque ornare consectetur</p><span class="more">Read more &rarr;</span></div>
  <div class="abs card" style="left:460px;top:716px"><div class="img" role="img" aria-label="Blue and tan fabric pattern swatch"></div><p>Uisque ornare consectetur</p><span class="more">Read more &rarr;</span></div>
</main>

<footer class="abs footer">
  <div class="abs fcol" style="left:129px;width:181px">
    <h2>FOOTER INFO</h2>
    <p style="line-height:17px;font-weight:600;width:181px">Lorem ipsum dolor sit amet, consectetur adipiscing elit. Curabitur vulputate imperdiet massa,</p>
    <p class="script">Join our mailing list</p>
    <div class="signup"><span>Enter your email address</span><i></i></div>
  </div>
  <div class="abs fcol" style="left:379px;width:142px">
    <h2>CONTACT INFO</h2>
    <ul>
      <li><svg width="10" height="10" viewBox="0 0 10 10"><path d="M1 5 5 1 9 5V9H1Z" fill="#dfe8ef"/></svg>48 Loom Lane</li>
      <li class="ind">Harbourvale</li>
      <li class="ind">5521904</li>
      <li><svg width="12" height="9" viewBox="0 0 12 9"><rect x=".5" y=".5" width="11" height="8" fill="#dfe8ef"/><path d="M.5 .5 6 5 11.5 .5" fill="none" stroke="#5e86a8"/></svg>hello@foldthread.com</li>
      <li class="ind">studio@foldthread.com</li>
      <li><svg width="10" height="10" viewBox="0 0 10 10"><rect width="10" height="10" fill="#dfe8ef"/><path d="M2 3h6M2 5h6M2 7h6" stroke="#5e86a8"/></svg>05550 441882</li>
    </ul>
  </div>
  <div class="abs fcol" style="left:568px;width:142px">
    <h2>SOCIAL MEDIA LINKS</h2>
    <ul>
      <li><span class="sq"></span>facenet.com/foldthread</li>
      <li><span class="sq"></span>chirper.com/foldthread</li>
      <li><span class="sq"></span>vidtube.com/foldthread</li>
      <li><span class="sq"></span>circlesplus/foldthread</li>
    </ul>
  </div>
</footer>

<div class="abs bar">
  <nav class="abs links"><span class="current">Home</span><span>Services</span><span>Brands</span><span>Process</span><span>Blog</span><span>Contact</span></nav>
  <p class="abs copy-note"><b>Copyright 2012</b> &nbsp; Allrights reserved</p>
</div>
</body>
</html>
```